Willowmere BTS LLC.

I need a business card design for my behavior therapy (ABA) company. I'm attaching the logo for our company. I'm also attaching the business card for our sister company (special needs school) for inspiration.

We would like a two sided business card created. Below please find our information.

We want the same puzzle piece ribbon with (blue, yellow, and red colors).

Address: 2719 Lindenfield Road Suite 204 West Palm Beach, FL 33519
Phone: 561-704-2198
email: Marla.p@willowmerebts.org
website: www.thewillowmereschool.org

```html
<!DOCTYPE html>
<html lang="en">
<head>
<meta charset="utf-8">
<title>Willowmere BTS LLC. – Business Card</title>
<link rel="stylesheet" href="https://fonts.googleapis.com/css2?family=Open+Sans:wght@400;600;700&display=swap">
<style>
  :root {
    --backdrop: #e9eaee;
    --card: #ffffff;
    --navy: #23348f;
    --blue: #1a78c8;
    --ink: #1f1f24;
    --shadow: rgba(20, 24, 40, 0.18);
  }
  * { box-sizing: border-box; margin: 0; padding: 0; }
  html, body {
    width: 1200px;
    height: 780px;
    overflow: hidden;
    background: var(--backdrop);
    font-family: "Open Sans", Arial, sans-serif;
  }
  .sheet {
    position: relative;
    width: 1200px;
    height: 780px;
  }
  .card {
    position: absolute;
    top: 230px;
    width: 540px;
    height: 320px;
    background: var(--card);
    border-radius: 30px;
    box-shadow: 0 10px 28px var(--shadow);
  }
  .card--contact { left: 40px; }
  .card--brand { left: 620px; }

  /* Brand side */
  .card--brand .brand-lockup {
    position: absolute;
    inset: 0;
    display: flex;
    align-items: center;
    justify-content: center;
    gap: 16px;
  }
  .brand-mark {
    width: 38px;
    height: 38px;
    border-radius: 50%;
    background: var(--navy);
    flex: none;
  }
  .brand-name {
    font-weight: 700;
    color: var(--navy);
    font-size: 40px;
    letter-spacing: 0.5px;
    white-space: nowrap;
  }

  /* Contact side */
  .card--contact .brand-lockup {
    position: absolute;
    left: 34px;
    top: 112px;
    display: flex;
    align-items: center;
    gap: 10px;
  }
  .card--contact .brand-mark { width: 20px; height: 20px; }
  .card--contact .brand-name { font-size: 21px; }

  .divider {
    position: absolute;
    left: 270px;
    top: 56px;
    width: 2px;
    height: 208px;
    background: var(--blue);
  }
  .contact {
    position: absolute;
    left: 292px;
    top: 62px;
    right: 20px;
    color: var(--ink);
  }
  .contact__name {
    font-weight: 700;
    font-size: 20px;
    color: var(--blue);
    letter-spacing: 0.3px;
    text-transform: uppercase;
  }
  .contact__name .first { color: var(--navy); }
  .contact__title {
    font-size: 13.5px;
    margin-bottom: 12px;
  }
  .contact__list { list-style: none; font-size: 12.5px; line-height: 1.65; }
  .contact__list li { display: flex; align-items: center; gap: 7px; white-space: nowrap; }
  .contact__list .icon { width: 12px; height: 12px; flex: none; fill: var(--blue); }
  .contact__list .indent { padding-left: 19px; }
  .contact__address { font-size: 12.5px; line-height: 1.55; margin-top: 8px; }
</style>
</head>
<body>
<main class="sheet">

  <section class="card card--contact" aria-label="Business card, contact side">
    <div class="brand-lockup">
      <span class="brand-mark" aria-hidden="true"></span>
      <span class="brand-name">Willowmere BTS</span>
    </div>

    <div class="divider" aria-hidden="true"></div>

    <div class="contact">
      <h1 class="contact__name"><span class="first">Daniel</span> Ortiz</h1>
      <p class="contact__title">Managing Director</p>
      <ul class="contact__list">
        <li>
          <svg class="icon" viewBox="0 0 24 24" aria-hidden="true"><path d="M6.6 10.8a15.1 15.1 0 0 0 6.6 6.6l2.2-2.2a1 1 0 0 1 1-.25 11.4 11.4 0 0 0 3.6.57 1 1 0 0 1 1 1V20a1 1 0 0 1-1 1A17 17 0 0 1 3 4a1 1 0 0 1 1-1h3.5a1 1 0 0 1 1 1c0 1.25.2 2.45.57 3.57a1 1 0 0 1-.25 1z"/></svg>
          561-704-2198
        </li>
        <li>
          <svg class="icon" viewBox="0 0 24 24" aria-hidden="true"><path d="M2 5h20v14H2z M2 5l10 8 10-8" fill="none" stroke="currentColor"/><path d="M2 5h20v2l-10 7L2 7z"/><path d="M2 8.5l10 7 10-7V19H2z"/></svg>
          Marla.p@willowmerebts.org
        </li>
        <li>
          <svg class="icon" viewBox="0 0 24 24" aria-hidden="true"><circle cx="12" cy="12" r="10"/><path d="M2 12h20M12 2c3 3 3 17 0 20M12 2c-3 3-3 17 0 20" stroke="#fff" stroke-width="1.4" fill="none"/></svg>
          www.willowmerebts.org
        </li>
        <li class="indent">www.thewillowmereschool.org</li>
      </ul>
      <p class="contact__address">2719 Lindenfield Road Suite 204<br>West Palm Beach, FL 33519</p>
    </div>
  </section>

  <section class="card card--brand" aria-label="Business card, brand side">
    <div class="brand-lockup">
      <span class="brand-mark" aria-hidden="true"></span>
      <span class="brand-name">Willowmere BTS LLC.</span>
    </div>
  </section>

</main>
</body>
</html>
```